Webdesign für Brandt Maler
Zielgruppe
Maler- und Bodenlegerarbeiten, Farbenherstellung, Fachmarkt
ZieIgruppe sind alle, die Fraben und/oder die Dienstleistungen der Firma benötigen
Aufgabenstellung
dem Kunde gefällt die Seite http://www.maler-quirinus.example/
bitte alle Uploads beachten
eigene Bilder und Stockmaterial

```html
<!DOCTYPE html>
<html lang="de">
<head>
<meta charset="utf-8">
<title>Brandt Maler – Auf gute Zusammenarbeit</title>
<link rel="stylesheet" href="https://fonts.googleapis.com/css2?family=Oxygen:wght@300;400&family=Varela+Round&display=swap">
<style>
  :root {
    --brand-pink: #e0195e;
    --brand-navy: #2d2f8c;
    --white: #ffffff;
    --ink: #2b2b2b;
    --nav-ink: #333333;
  }
  * { box-sizing: border-box; margin: 0; padding: 0; }
  html, body {
    width: 1200px;
    height: 505px;
    overflow: hidden;
    background: var(--brand-pink);
  }
  .page {
    position: relative;
    width: 1200px;
    height: 505px;
    font-family: "Oxygen", sans-serif;
  }
  .site-header {
    position: absolute;
    top: 0; left: 0;
    width: 1200px;
    height: 66px;
    background: var(--white);
    box-shadow: inset 0 2px 3px rgba(0,0,0,0.35);
  }
  .brand {
    position: absolute;
    left: 33px;
    top: 20px;
    display: flex;
    align-items: center;
    gap: 8px;
    font-family: "Varela Round", sans-serif;
    font-size: 22px;
    color: var(--brand-navy);
    letter-spacing: 0.2px;
  }
  .brand-dot {
    width: 14px;
    height: 14px;
    border-radius: 50%;
    background: var(--brand-navy);
  }
  .main-nav {
    position: absolute;
    top: 24px;
    left: 0;
    font-size: 15px;
    color: var(--nav-ink);
  }
  .main-nav a {
    position: absolute;
    white-space: nowrap;
    color: inherit;
    text-decoration: none;
  }
  .main-nav .is-active { left: 466px; padding-bottom: 2px; border-bottom: 2px solid var(--nav-ink); }
  .main-nav .nav-services { left: 538px; }
  .main-nav .nav-contact { left: 672px; }
  .cta-header {
    position: absolute;
    left: 966px;
    top: 17px;
    width: 188px;
    height: 33px;
    border-radius: 3px;
    background: var(--brand-pink);
    color: var(--white);
    font-size: 15px;
    display: flex;
    align-items: center;
    justify-content: center;
  }
  .hero {
    position: absolute;
    top: 66px;
    left: 0;
    width: 1200px;
    text-align: center;
    color: var(--white);
  }
  .hero-title {
    margin-top: 74px;
    font-family: "Varela Round", sans-serif;
    font-weight: 400;
    font-size: 33px;
    line-height: 44px;
  }
  .hero-text {
    width: 500px;
    margin: 17px auto 0;
    font-size: 15.5px;
    font-weight: 300;
    line-height: 24.5px;
  }
  .hero-button {
    display: inline-flex;
    align-items: center;
    justify-content: center;
    margin-top: 31px;
    width: 155px;
    height: 42px;
    border-radius: 3px;
    background: var(--white);
    color: var(--ink);
    font-size: 15px;
  }
  .corner-widget {
    position: absolute;
    left: 28px;
    top: 499px;
    width: 178px;
    height: 10px;
    background: var(--white);
    border-radius: 2px 2px 0 0;
  }
  .corner-widget::after {
    content: "";
    position: absolute;
    left: 92px;
    top: 5px;
    width: 70px;
    height: 1px;
    background: #1f3b3a;
  }
</style>
</head>
<body>
<div class="page">
  <header class="site-header">
    <div class="brand"><span>Brandt Maler</span><span class="brand-dot"></span></div>
    <nav class="main-nav">
      <a class="is-active" href="#">Home</a>
      <a class="nav-services" href="#">Unsere Leistung</a>
      <a class="nav-contact" href="#">Kontakt</a>
    </nav>
    <a class="cta-header">Gespräch vereinbaren</a>
  </header>

  <section class="hero">
    <h1 class="hero-title">Auf gute Zusammenarbeit</h1>
    <p class="hero-text">Wir freuen uns, dass Sie sich für unsere Firma interessieren und laden Sie recht herzlich ein, unser Unternehmen, unsere Serviceleistungen und unsere Produkte näher kennen zu lernen.</p>
    <a class="hero-button">Mit uns arbeiten</a>
  </section>

  <div class="corner-widget"></div>
</div>
</body>
</html>
```